Letterhead Design Project

I need letterhead designed for my law firm. It would also be used for web based stuff as well.

Industry/Entity Type

Law Firm

```html
<!DOCTYPE html>
<html lang="en">
<head>
<meta charset="utf-8">
<title>Hartwell &amp; Moss Law Firm — Letterhead</title>
<link rel="stylesheet" href="https://fonts.googleapis.com/css2?family=Cinzel:wght@600&family=Jost:wght@400&display=swap">
<style>
  :root {
    --brand-blue: #126a94;
    --paper: #ffffff;
    --footer-text: #ffffff;
  }
  * { margin: 0; padding: 0; box-sizing: border-box; }
  html, body {
    width: 849px;
    height: 1200px;
    overflow: hidden;
    background: var(--paper);
  }
  .letterhead {
    position: relative;
    width: 849px;
    height: 1200px;
    background: var(--paper);
  }
  .brand-disc {
    position: absolute;
    left: 323px;
    top: 0;
    width: 202px;
    height: 102px;
  }
  .firm-name {
    position: absolute;
    top: 110px;
    left: 0;
    width: 100%;
    text-align: center;
    font-family: "Cinzel", serif;
    font-weight: 600;
    color: var(--brand-blue);
    font-size: 30px;
    letter-spacing: 0.5px;
    line-height: 36px;
  }
  .firm-descriptor {
    position: absolute;
    top: 152px;
    left: 0;
    width: 100%;
    text-align: center;
    font-family: "Cinzel", serif;
    font-weight: 600;
    color: var(--brand-blue);
    font-size: 13px;
    letter-spacing: 14px;
    padding-left: 14px;
    line-height: 18px;
  }
  .contact-band {
    position: absolute;
    left: 0;
    bottom: 0;
    width: 100%;
    height: 62px;
    background: var(--brand-blue);
    display: flex;
    align-items: center;
    justify-content: center;
    font-family: "Jost", sans-serif;
    font-weight: 400;
    color: var(--footer-text);
    font-size: 13.5px;
    letter-spacing: 3px;
    white-space: nowrap;
  }
  .contact-band .sep { margin: 0 10px; }
</style>
</head>
<body>
  <main class="letterhead">
    <svg class="brand-disc" viewBox="0 0 202 102" aria-hidden="true">
      <circle cx="101" cy="0" r="101" fill="var(--brand-blue)"/>
    </svg>
    <h1 class="firm-name">Hartwell &amp; Moss</h1>
    <p class="firm-descriptor">LAW FIRM</p>

    <footer class="contact-band">
      <span class="sep">•</span>
      <span class="address">820 ALDER ST NW #310, WASHINGTON, DC 20001</span>
      <span class="sep">•</span>
      <span class="phone">T: (202) 555-0147</span>
      <span class="sep">•</span>
    </footer>
  </main>
</body>
</html>
```